Brightmere Realty information card

We need a 5x7 two-sided card to hand out at open houses and provide to our charitable partners for distribution. We are a local real estate group looking to add a "give back" component to our business. We are located in a coastal community and would like to incorporate that feel into our design. We are giving clients who use us the ability to designate 1 out of the 10 charitable organizations we partner with - and we will make a donation to that organization.

We included the 10 partner logos below - we envision them pretty small. Also included 2 photos of the "Brightmere" and our logo. Have fun.
Updates

Project Deadline Extended
Reason: We're out of town until Wednesday, May 17th.

Target Market(s)

home buyers & sellers

Industry/Entity Type

Real Estate

Font styles to use
Serif
Sans Serif

Colors

Designer to choose colors to be used in the design.

Requirements
Must have
• slogan & tagline - see attached text file
• Brightmere photo
Nice to have
• partner logos - small - maybe in circles?

```html
<!DOCTYPE html>
<html lang="en">
<head>
<meta charset="utf-8">
<title>Brightmere Realty – Information Card</title>
<link rel="stylesheet" href="https://fonts.googleapis.com/css2?family=Josefin+Sans:wght@400;600&family=Arimo:wght@400;700&display=swap">
<style>
  :root {
    --backdrop: #a9d8f7;
    --card: #ffffff;
    --ink: #111111;
    --navy: #3d5a80;
    --accent-blue: #5a82c4;
    --slate: #58595b;
    --band-black: #0d0d0d;
    --partner-panel: #c8d2e5;
    --partner-dot: #7a7f8c;
    --white: #ffffff;
  }
  * { box-sizing: border-box; margin: 0; padding: 0; }
  html, body { width: 1200px; height: 841px; overflow: hidden; }
  body { background: var(--backdrop); font-family: "Arimo", Arial, sans-serif; position: relative; }

  .card { position: absolute; top: 124px; width: 424px; height: 598px; background: var(--card); overflow: hidden; box-shadow: 0 4px 14px rgba(0,0,0,.18); }
  .card--front { left: 178px; }
  .card--back { left: 634px; }

  .photo { position: absolute; left: 0; top: 0; width: 100%; }
  .photo--sunset { height: 416px; background: linear-gradient(180deg, #a07a9a 0%, #e58f86 22%, #f0a08a 38%, #c9848c 52%, #6a4c66 66%, #3a2c3c 82%, #2a2230 100%); }
  .photo--daytime { height: 350px; background: linear-gradient(180deg, #6fa3d6 0%, #cfe0ef 25%, #e9eef2 45%, #8fb0c8 60%, #9aa08e 72%, #6b7460 88%, #8a3a35 100%); }

  .brand-box { position: absolute; left: 74px; top: 0; width: 118px; height: 168px; background: var(--slate); display: flex; flex-direction: column; align-items: center; justify-content: flex-end; padding-bottom: 16px; }
  .brand-box__mark { width: 14px; height: 14px; background: var(--accent-blue); margin-bottom: 8px; }
  .brand-box__name { font-family: "Arimo", Arial, sans-serif; font-size: 17px; color: var(--white); text-align: center; line-height: 1.15; }

  .headline { position: absolute; font-family: "Josefin Sans", Arial, sans-serif; text-transform: uppercase; }
  .headline--front { left: 204px; top: 16px; color: var(--white); font-size: 33px; line-height: 1.0; letter-spacing: .5px; }
  .tagline { position: absolute; left: 204px; top: 140px; width: 130px; font-family: "Arimo", Arial, sans-serif; font-size: 10px; color: var(--white); line-height: 1.25; }
  .headline--back { left: 44px; top: 40px; color: var(--navy); font-size: 38px; font-weight: 600; line-height: 1.08; }

  .pledge { position: absolute; left: 16px; top: 432px; width: 396px; font-size: 14.5px; line-height: 1.3; color: var(--ink); text-align: justify; }
  .pledge strong { font-weight: 700; font-size: 15px; }

  .statement { position: absolute; left: 10px; top: 360px; width: 404px; font-size: 10.4px; line-height: 1.32; color: var(--ink); text-align: justify; text-align-last: center; }
  .referral { position: absolute; left: 0; top: 442px; width: 100%; text-align: center; font-size: 11.5px; color: var(--ink); }

  .together { position: absolute; left: 24px; top: 466px; width: 150px; text-align: center; font-family: "Josefin Sans", Arial, sans-serif; font-size: 17px; line-height: 1.2; color: var(--navy); text-transform: uppercase; }

  .partners { position: absolute; left: 196px; top: 466px; width: 222px; height: 76px; background: var(--partner-panel); display: grid; grid-template-columns: repeat(5, 30px); grid-template-rows: repeat(2, 30px); gap: 6px 13px; justify-content: center; align-content: center; }
  .partners__badge { width: 30px; height: 30px; border-radius: 50%; background: var(--partner-dot); }

  .footer-band { position: absolute; left: 0; bottom: 0; width: 100%; height: 30px; background: var(--band-black); }
  .footer-tab { position: absolute; background: var(--accent-blue); color: var(--band-black); display: flex; align-items: center; clip-path: polygon(5% 0, 100% 0, 100% 100%, 0 100%); }
  .footer-tab--web { left: 192px; bottom: 6px; width: 222px; height: 40px; justify-content: center; font-weight: 700; font-size: 13px; padding-left: 10px; }
  .footer-tab--contacts { left: 126px; bottom: 4px; width: 290px; height: 40px; flex-direction: column; justify-content: center; font-size: 11.5px; line-height: 1.3; padding-left: 16px; font-family: "Josefin Sans", Arial, sans-serif; }
  .contact__name { font-weight: 600; }
</style>
</head>
<body>

<section class="card card--front">
  <div class="photo photo--sunset" role="img" aria-label="Photo of the coastal town at sunset, with a pink sky over the bay and city lights below"></div>
  <div class="brand-box">
    <span class="brand-box__mark"></span>
    <span class="brand-box__name">Brightmere<br>Realty</span>
  </div>
  <h1 class="headline headline--front">Change<br>Homes,<br>Change<br>Lives</h1>
  <p class="tagline">Changing the World One Home at a Time</p>
  <p class="pledge"><strong>Because we value generosity and desire to make a difference in our community and world,</strong> for every home bought or sold through us, we will make a contribution to one of our amazing partner who are helping to change the world.</p>
  <div class="footer-band"></div>
  <div class="footer-tab footer-tab--web">www.brightmererealty.com</div>
</section>

<section class="card card--back">
  <div class="photo photo--daytime" role="img" aria-label="Photo of the coastal town by day, with blue sky, clouds, the bay and red flowers in the foreground"></div>
  <h2 class="headline headline--back">We live<br>here.<br>We give<br>here.</h2>
  <p class="statement">We give because we value generosity and believe we have been blessed to be a blessing. We believe that together we can change the world one home at time. You have our guarantee of personal service and no additional costs. The donations come out of our commission, not your pocket. You get to designate which of our amazing partner organizations you would like us to contribute to on behalf of your transaction. When you are ready to buy or sell, please consider giving us a call.</p>
  <p class="referral">Tell a friend about us too.</p>
  <p class="together">Together,<br>we can make<br>the world<br>a better place.</p>
  <div class="partners" aria-label="Partner organizations">
    <span class="partners__badge"></span><span class="partners__badge"></span><span class="partners__badge"></span><span class="partners__badge"></span><span class="partners__badge"></span>
    <span class="partners__badge"></span><span class="partners__badge"></span><span class="partners__badge"></span><span class="partners__badge"></span><span class="partners__badge"></span>
  </div>
  <div class="footer-band"></div>
  <div class="footer-tab footer-tab--contacts">
    <span class="contact"><span class="contact__name">DANIEL HARLOW</span> – daniel@brightmererealty.com</span>
    <span class="contact"><span class="contact__name">MARIE HARLOW</span> – marie@brightmererealty.com</span>
  </div>
</section>

</body>
</html>
```